This is a label for a new sake made in Japan imported into Aust

This will be a bottle label for a new sake imported into Australia. The hero of the label is the Velmora. We have joined the "O" meaning great in Japanese and used sake with "Z" to have Velmora with the play on words using Oz as in our slang for Aussie. A modern label with a Japanese take is key. This is a premium sake made in Japan for the Australian market.
The "Tall Casks" up the top is the name of the company, we have yet to design a logo for the company.

Target Market(s)

Alcohol

Logo Text

Velmora

Font styles to use
Serif

Requirements
Must have
• easy to read, with a hint of Japanese origin
Should not have
• too busy

```html
<!DOCTYPE html>
<html lang="en">
<head>
<meta charset="utf-8">
<title>Velmora – Premium Japanese Sake Label</title>
<link href="https://fonts.googleapis.com/css2?family=Staatliches&family=Poiret+One&family=Noto+Serif+JP:wght@400&display=swap" rel="stylesheet">
<style>
  :root {
    --label-red: #ff0000;
    --label-white: #ffffff;
    --ink: #111111;
    --kanji-grey: #e2e2e2;
  }
  * { margin: 0; padding: 0; box-sizing: border-box; }
  html, body { width: 968px; height: 1200px; overflow: hidden; background: var(--label-white); }
  .label {
    position: relative;
    width: 968px;
    height: 1200px;
    background: var(--label-red);
  }
  .label__panel {
    position: absolute;
    left: 55px; top: 57px;
    width: 855px; height: 1088px;
    background: var(--label-white);
  }
  .company-name {
    position: absolute;
    left: 212px; top: 96px;
    width: 540px;
    display: flex;
    justify-content: space-between;
    font-family: "Staatliches", sans-serif;
    font-size: 62px;
    line-height: 1;
    color: var(--ink);
  }
  .ornament {
    position: absolute;
    background: var(--label-red);
    opacity: 0.85;
  }
  .ornament--left  { left: 147px; top: 92px; width: 36px; height: 68px; border-radius: 18px; }
  .ornament--right { left: 784px; top: 92px; width: 36px; height: 68px; border-radius: 18px; }
  .ornament--blossom { left: 347px; top: 313px; width: 275px; height: 137px; border-radius: 120px 120px 10px 10px; }
  .ornament--under { left: 431px; top: 713px; width: 111px; height: 58px; border-radius: 0 0 55px 55px; }
  .rule {
    position: absolute;
    height: 11px;
    background: var(--label-red);
  }
  .rule--top { left: 117px; top: 456px; width: 738px; }
  .rule--bottom { left: 114px; top: 699px; width: 737px; }
  .brand-mark {
    position: absolute;
    left: 118px; top: 490px;
    width: 737px; height: 190px;
    display: flex;
    align-items: center;
    gap: 22px;
  }
  .brand-mark__dot {
    width: 186px; height: 186px;
    border-radius: 50%;
    background: var(--ink);
    flex: none;
  }
  .brand-mark__name {
    font-family: "Poiret One", sans-serif;
    font-size: 124px;
    line-height: 1;
    color: var(--ink);
  }
  .kanji {
    position: absolute;
    left: 72px; top: 800px;
    width: 820px;
    display: flex;
    justify-content: space-between;
    font-family: "Noto Serif JP", serif;
    font-size: 225px;
    line-height: 1.2;
    color: var(--kanji-grey);
  }
  .product-type {
    position: absolute;
    left: 0; top: 842px;
    width: 968px;
    text-align: center;
    font-family: "Poiret One", sans-serif;
    font-size: 63px;
    line-height: 69px;
    color: var(--ink);
    -webkit-text-stroke: 1.4px var(--ink);
  }
  .product-type__dot {
    position: absolute;
    left: 482px; top: 1054px;
    width: 10px; height: 10px;
    border-radius: 50%;
    background: var(--ink);
  }
</style>
</head>
<body>
  <div class="label">
    <div class="label__panel"></div>

    <div class="ornament ornament--left" role="img" aria-label="Small red flourish ornament"></div>
    <div class="company-name" aria-label="Tall Casks">
      <span>T</span><span>A</span><span>L</span><span>L</span><span>C</span><span>A</span><span>S</span><span>K</span><span>S</span>
    </div>
    <div class="ornament ornament--right" role="img" aria-label="Small red flourish ornament"></div>

    <div class="ornament ornament--blossom" role="img" aria-label="Red cherry blossom ornament"></div>
    <div class="rule rule--top"></div>

    <div class="brand-mark">
      <div class="brand-mark__dot"></div>
      <div class="brand-mark__name">Velmora</div>
    </div>

    <div class="rule rule--bottom"></div>
    <div class="ornament ornament--under" role="img" aria-label="Small red flourish ornament"></div>

    <div class="kanji" aria-hidden="true"><span>日</span><span>本</span><span>酒</span></div>

    <div class="product-type">PREMIUM<br>JAPANESE<br>SAKE</div>
    <div class="product-type__dot"></div>
  </div>
</body>
</html>
```